Modern Corvane Tree Care Website

I need a website for a full service Tree Care company. The company provides tree pruning, tree removal, tree preservation, emergency services, stump grinding, and emergency tree services.

Target Market(s)

Customers that need tree services

Industry/Entity Type

Landscaping, Tree Services

Coding

Coded - Design and coding required

Number of Pages Required

5+ page

Font styles to use
Sans Serif

Requirements
Must have
• Good clean design that showcases the services the company provides.
Nice to have
• Services page; contact form, blog, home page, about page

```html
<!DOCTYPE html>
<html lang="en">
<head>
<meta charset="utf-8">
<title>Corvane Tree Care</title>
<link href="https://fonts.googleapis.com/css2?family=Ubuntu:wght@400;500;700&family=Lato:wght@400;700;900&display=swap" rel="stylesheet">
<style>
:root{
  --navy:#111a3b;
  --navy-deep:#0c1330;
  --navy-bar:#1a2248;
  --green:#8cc63f;
  --green-dark:#6fa52b;
  --blue:#1d4a8a;
  --orange:#f29a3a;
  --text:#2b2f3a;
  --muted:#8a8f9c;
  --white:#ffffff;
  --photo-dark:#2a3320;
  --sky:#cdeefc;
}
*{box-sizing:border-box;margin:0;padding:0}
html,body{width:1200px;height:4881px;overflow:hidden;background:var(--white)}
body{font-family:"Lato",sans-serif;color:var(--text)}
.page{position:relative;width:1200px;height:4881px;overflow:hidden}
.abs{position:absolute}
h1,h2,h3,.heading{font-family:"Ubuntu",sans-serif}
.btn{position:absolute;background:var(--green);color:var(--white);font-weight:700;font-size:14px;display:flex;align-items:center;justify-content:center;gap:12px;border-radius:2px}
.eyebrow{position:absolute;font-size:12px;color:var(--green);text-transform:uppercase;letter-spacing:.3px;text-decoration:underline;text-underline-offset:3px}
.photo{position:absolute}

/* header */
.topbar{position:absolute;left:389px;top:0;width:811px;height:32px;background:var(--navy);color:var(--white);font-size:11px;font-weight:700;display:flex;align-items:center}
.topbar-appt{position:absolute;left:204px;top:0;width:234px;height:32px;background:var(--green);display:flex;align-items:center;justify-content:center;gap:8px;font-weight:400;font-size:10px}
.topbar-item{position:absolute;display:flex;align-items:center;gap:8px}
.logo{position:absolute;left:118px;top:28px;display:flex;align-items:center;gap:12px}
.logo-mark{width:48px;height:48px;background:var(--green)}
.logo-name{font-family:"Ubuntu",sans-serif;font-weight:700;font-size:26px;color:var(--navy);line-height:1}
.nav a{position:absolute;top:60px;font-size:12px;font-weight:700;color:#3a3f4d;text-decoration:none}
.header-cta{position:absolute;left:931px;top:53px;width:118px;height:32px;border:1.5px solid var(--orange);border-radius:3px;color:var(--orange);font-size:11px;display:flex;align-items:center;justify-content:center}

/* hero */
.hero{position:absolute;left:0;top:102px;width:1200px;height:691px;background:linear-gradient(160deg,#3a4630 0%,#2a3323 45%,#1e2519 100%)}
.hero-tag{position:absolute;left:0;width:1200px;top:213px;text-align:center;color:var(--white);font-size:12px;letter-spacing:.3px}
.hero-tag::before,.hero-tag::after{content:"";display:inline-block;width:34px;height:2px;background:var(--green);vertical-align:middle;margin:0 44px}
.hero h1{position:absolute;left:0;width:1200px;top:240px;text-align:center;color:var(--white);font-size:54px;font-weight:500;line-height:60px}
.hero-sub{position:absolute;left:0;width:1200px;top:386px;text-align:center;color:var(--white);font-size:14px;font-weight:700}

.wave{position:absolute;left:0;width:1200px}

/* about */
.about-title{position:absolute;left:618px;top:1008px;font-size:38px;font-weight:500;color:var(--navy);line-height:46px}
.about-sub{position:absolute;left:618px;top:1128px;font-size:20px;color:var(--navy);font-family:"Ubuntu",sans-serif}
.para{position:absolute;font-size:12.5px;line-height:20px;color:var(--muted)}

/* services */
.dark{position:absolute;left:0;width:1200px;background:linear-gradient(180deg,#2b2b25 0%,#1f211c 60%,#191b17 100%)}
.section-title{position:absolute;left:0;width:1200px;text-align:center;font-size:44px;font-weight:500}
.card-img{position:absolute;width:283px;height:279px}
.card-icon{position:absolute;width:74px;height:72px;background:var(--white);display:flex;align-items:center;justify-content:center}
.card-title{position:absolute;width:283px;text-align:center;color:var(--white);font-weight:700;font-size:16px}
.card-text{position:absolute;width:283px;text-align:center;color:#e6e6e6;font-size:13px;line-height:21px}

/* faq */
.faq-title{position:absolute;left:154px;top:2422px;font-size:38px;font-weight:700;color:var(--blue);line-height:49px;letter-spacing:.5px}
.faq-q{position:absolute;left:537px;font-size:15px;font-weight:700;color:var(--blue)}
.faq-line{position:absolute;left:537px;width:508px;height:1.5px;background:#cfd4dc}
.faq-toggle{position:absolute;left:993px;width:50px;height:50px;border-radius:50%;display:flex;align-items:center;justify-content:center;color:var(--white);font-size:20px}
.faq-answer{position:absolute;left:537px;top:2552px;width:460px;font-size:14.5px;line-height:26px;color:#777c88}

/* professionals */
.feature{position:absolute;display:flex;gap:18px;color:var(--white)}
.feature h4{font-size:16px;font-weight:700;margin-top:-2px}
.feature p{font-size:12px;line-height:20px;color:#d9d9d9;margin-top:6px}

/* testimonials */
.quote-box{position:absolute;left:131px;top:3915px;width:940px;height:205px;border:1.5px solid #d7d9de}
.avatar{position:absolute;border-radius:50%;background:linear-gradient(160deg,#b7bcc4,#6c717a)}

/* footer */
.footer{position:absolute;left:0;top:4281px;width:1200px;height:544px;background:var(--navy)}
.social{position:absolute;top:4423px;width:38px;height:38px;border-radius:3px;display:flex;align-items:center;justify-content:center}
.contact-item{position:absolute;top:4702px;display:flex;align-items:center;gap:18px;color:var(--white)}
.contact-item small{display:block;font-size:15px;color:#c9ccd6}
.contact-item strong{display:block;font-size:16px;font-weight:700;margin-top:4px}
.bottombar{position:absolute;left:0;top:4825px;width:1200px;height:56px;background:var(--navy-bar);color:var(--white);font-size:13px}
.bottombar span{position:absolute;top:20px}
</style>
</head>
<body>
<div class="page">

  <!-- header -->
  <header>
    <div class="logo"><span class="logo-mark"></span><span class="logo-name">Corvane Tree Care</span></div>
    <div class="topbar">
      <div class="topbar-item" style="left:53px">
        <svg width="14" height="14" viewBox="0 0 24 24" fill="none" stroke="#fff" stroke-width="2"><path d="M22 16.9v3a2 2 0 0 1-2.2 2 19.8 19.8 0 0 1-8.6-3.1 19.5 19.5 0 0 1-6-6A19.8 19.8 0 0 1 2.1 4.2 2 2 0 0 1 4.1 2h3a2 2 0 0 1 2 1.7c.1.9.4 1.8.7 2.7a2 2 0 0 1-.5 2.1L8 9.8a16 16 0 0 0 6 6l1.3-1.3a2 2 0 0 1 2.1-.5c.9.3 1.8.6 2.7.7a2 2 0 0 1 1.7 2z"/></svg>
        512 - 555 - 0148
      </div>
      <div class="topbar-appt">
        <svg width="14" height="14" viewBox="0 0 24 24" fill="none" stroke="#fff" stroke-width="2"><rect x="3" y="4" width="18" height="18" rx="2"/><path d="M16 2v4M8 2v4M3 10h18"/></svg>
        REQUEST AN APPOINTMENT
      </div>
      <div class="topbar-item" style="left:473px;font-weight:400;font-size:10.5px">
        <svg width="12" height="14" viewBox="0 0 24 24" fill="none" stroke="#fff" stroke-width="2"><path d="M12 22s7-7.5 7-13a7 7 0 0 0-14 0c0 5.5 7 13 7 13z"/><circle cx="12" cy="9" r="2.5"/></svg>
        4820 Cedar Hollow Lane
      </div>
    </div>
    <nav class="nav">
      <a style="left:396px">Home</a>
      <a style="left:465px">Services</a>
      <a style="left:546px">About Us</a>
      <a style="left:622px">Giving Back</a>
      <a style="left:713px">And more</a>
      <a style="left:796px">Login</a>
    </nav>
    <div class="header-cta">CONTACT US</div>
  </header>

  <!-- hero -->
  <section class="hero" role="img" aria-label="Arborist climbing a tree trunk in a forest, darkened background photo">
    <p class="hero-tag">WE TARE THE BEST IN TOWN</p>
    <h1>We Offer Sustainable<br>Tree Solutions</h1>
    <p class="hero-sub">Top Rated Tree Experts in the City</p>
    <div class="btn" style="left:508px;top:436px;width:159px;height:42px;font-weight:400;font-size:13px">More Details</div>
  </section>
  <svg class="wave" style="top:713px" height="82" viewBox="0 0 1200 82" preserveAspectRatio="none">
    <path d="M0 64 Q600 -10 1200 64 L1200 82 L0 82Z" fill="#fff"/>
    <path d="M110 10 Q600 72 1090 10 Q600 54 110 10Z" fill="var(--green)"/>
  </svg>

  <!-- about -->
  <section>
    <div class="abs" style="left:78px;top:1003px;width:164px;height:164px;border-radius:50%;background:var(--sky)"></div>
    <div class="photo" role="img" aria-label="Arborist cutting a large branch with a chainsaw" style="left:201px;top:908px;width:364px;height:419px;border-radius:18px;background:linear-gradient(150deg,#6a5a44,#3e4a2c 55%,#8a8a78)"></div>
    <div class="abs" style="left:125px;top:1105px;width:343px;height:336px;border-radius:22px;background:#fff;box-shadow:0 4px 14px rgba(0,0,0,.12)"></div>
    <div class="photo" role="img" aria-label="Climber in harness and helmet working up in a bare tree" style="left:139px;top:1119px;width:315px;height:308px;border-radius:16px;background:linear-gradient(170deg,#c9dbe9,#9fb3c2 50%,#5d6b76)"></div>

    <p class="eyebrow" style="left:618px;top:977px">Who we are</p>
    <h2 class="about-title">Your Partner in Tree<br>Presevation</h2>
    <p class="about-sub">Enhancing Landscapes, One Tree at a Time</p>
    <p class="para" style="left:618px;top:1165px;width:455px">Lorem ipsum dolor sit amet, consectetur adipiscing elit, sed do eiusmod temp or incididunt ut labore et dolore magna aliqua. Ut enim ad minim veniam, quis laboris nisi ut aliquip ex ea commodo consequat.</p>
    <p class="para" style="left:618px;top:1234px;width:455px">Lorem ipsum dolor sit amet, consectetur adipiscing elit, sed do eiusmod temp or incididunt ut labore et dolore magna aliqua.</p>
    <div class="btn" style="left:618px;top:1299px;width:137px;height:40px">Contact us
      <svg width="16" height="12" viewBox="0 0 16 12" fill="none" stroke="#fff" stroke-width="1.6"><path d="M1 6h13M9 1l5 5-5 5"/></svg>
    </div>
  </section>

  <!-- services -->
  <section class="dark" style="top:1507px;height:793px" role="img" aria-label="Dark forest background photo">
  </section>
  <svg class="wave" style="top:1507px" height="80" viewBox="0 0 1200 80" preserveAspectRatio="none">
    <path d="M0 0 L1200 0 L1200 6 Q600 100 0 6Z" fill="#fff"/>
    <path d="M110 20 Q600 92 1090 20 Q600 74 110 20Z" fill="var(--green)"/>
  </svg>
  <p class="eyebrow" style="left:0;width:1200px;text-align:center;top:1646px;color:#fff">Our services</p>
  <h2 class="section-title" style="top:1682px;color:#fff">Services We Provide</h2>

  <div class="card-img" role="img" aria-label="Worker pruning branches with long-handled loppers" style="left:119px;top:1778px;background:linear-gradient(160deg,#6f8a4a,#3d4a2a 60%,#d8d8d0)"></div>
  <div class="card-img" role="img" aria-label="Freshly cut tree trunk lying on the ground" style="left:447px;top:1778px;background:linear-gradient(160deg,#9b8a4a,#6a5a32 55%,#3f4a2a)"></div>
  <div class="card-img" role="img" aria-label="Two gardeners tending a row of hedges" style="left:775px;top:1778px;background:linear-gradient(160deg,#3d6a32,#5e8a44 55%,#8a7a5a)"></div>

  <div class="card-icon" style="left:349px;top:1803px">
    <svg width="34" height="34" viewBox="0 0 24 24" fill="none" stroke="var(--green)" stroke-width="1.4"><path d="M4 20h16M7 20c0-4 3-6 6-6M12 14l6-8M15 5l4 3"/><circle cx="11" cy="10" r="2"/></svg>
  </div>
  <div class="card-icon" style="left:677px;top:1803px">
    <svg width="34" height="34" viewBox="0 0 24 24" fill="none" stroke="var(--green)" stroke-width="1.4"><circle cx="12" cy="13" r="8"/><path d="M12 13l3-4M8 9l1 1M16 9l-1 1M12 6v2"/></svg>
  </div>
  <div class="card-icon" style="left:1005px;top:1803px">
    <svg width="34" height="34" viewBox="0 0 24 24" fill="none" stroke="var(--green)" stroke-width="1.4"><path d="M12 3l2.6 5.3 5.9.9-4.3 4.1 1 5.8L12 16.3 6.8 19.1l1-5.8L3.5 9.2l5.9-.9z"/></svg>
  </div>

  <h3 class="card-title" style="left:119px;top:2080px">Tree Pruning</h3>
  <h3 class="card-title" style="left:447px;top:2080px">Tree Removal</h3>
  <h3 class="card-title" style="left:775px;top:2080px">Stump Grinding</h3>
  <p class="card-text" style="left:119px;top:2112px">Lorem ipsum dolor sit amet, consectetur adipiscing elit, sed do ei</p>
  <p class="card-text" style="left:447px;top:2112px">Lorem ipsum dolor sit amet, consectetur adipiscing elit, sed do ei</p>
  <p class="card-text" style="left:775px;top:2112px">Lorem ipsum dolor sit amet, consectetur adipiscing elit, sed do ei</p>

  <svg class="wave" style="top:2218px" height="82" viewBox="0 0 1200 82" preserveAspectRatio="none">
    <path d="M0 64 Q600 -10 1200 64 L1200 82 L0 82Z" fill="#fff"/>
    <path d="M110 40 Q600 -14 1090 40 Q600 6 110 40Z" fill="var(--green)"/>
  </svg>

  <!-- faq -->
  <section>
    <div class="abs" style="left:154px;top:2391px;width:11px;height:11px;background:var(--green)"></div>
    <p class="abs" style="left:181px;top:2387px;font-size:14px;font-weight:700;color:var(--blue)">FAQ</p>
    <h2 class="faq-title">FREQUENTLY<br>ASKED QUESTIONS</h2>
    <div class="photo" role="img" aria-label="Arborist cutting a branch high in a tree against a blue sky" style="left:154px;top:2546px;width:324px;height:321px;border-radius:6px 6px 6px 22px;background:linear-gradient(170deg,#5d9bd6,#2d74c4 60%,#5c5a3c)"></div>

    <p class="faq-q" style="top:2417px">How do I get consultations started?</p>
    <div class="faq-toggle" style="top:2402px;background:var(--blue)">+</div>
    <div class="faq-line" style="top:2472px"></div>

    <p class="faq-q" style="top:2514px">How do I get consultations started?</p>
    <div class="faq-toggle" style="top:2497px;background:var(--green)">–</div>
    <p class="faq-answer">Lorem ipsum dolor sit amet, consectetur adipiscing elit, sed do eiusmod tempor incididunt ut labore et dolore magna aliqua. Ut enim ad minim veniam, Lorem ipsum dolor sit amet consectetur</p>
    <div class="faq-line" style="top:2675px"></div>

    <p class="faq-q" style="top:2714px">How do I get consultations started?</p>
    <div class="faq-toggle" style="top:2699px;background:var(--blue)">+</div>
    <div class="faq-line" style="top:2772px"></div>

    <p class="faq-q" style="top:2811px">How do I get consultations started?</p>
    <div class="faq-toggle" style="top:2796px;background:var(--blue)">+</div>
    <div class="faq-line" style="top:2869px"></div>
  </section>

  <!-- professionals -->
  <section class="dark" style="top:2967px;height:787px" role="img" aria-label="Dark forest background photo"></section>
  <svg class="wave" style="top:2967px" height="80" viewBox="0 0 1200 80" preserveAspectRatio="none">
    <path d="M0 0 L1200 0 L1200 6 Q600 100 0 6Z" fill="#fff"/>
    <path d="M110 20 Q600 92 1090 20 Q600 74 110 20Z" fill="var(--green)"/>
  </svg>
  <div class="photo" role="img" aria-label="Two smiling engineers in hard hats and safety vests holding plans" style="left:645px;top:3110px;width:555px;height:606px;background:linear-gradient(180deg,rgba(230,230,225,.25),rgba(200,210,60,.35) 55%,rgba(60,80,120,.35))"></div>
  <p class="eyebrow" style="left:129px;top:3150px">Who we are</p>
  <h2 class="abs heading" style="left:129px;top:3180px;font-size:40px;font-weight:500;color:#fff;line-height:47px">Your Tree Care<br>Professionals</h2>
  <p class="para" style="left:129px;top:3288px;width:460px;color:#e4e4e4;font-size:12px;line-height:19px">Lorem ipsum dolor sit amet, consectetur adipiscing elit, sed do eiusmod temp or incididunt ut labore et dolore magna aliqua. Ut enim ad minim veniam, quis laboris nisi ut aliquip ex ea commodo consequat.</p>

  <div class="feature" style="left:129px;top:3380px">
    <svg width="32" height="32" viewBox="0 0 24 24" fill="none" stroke="#fff" stroke-width="1.8"><path d="M20 12v8H4V4h11"/><path d="M8 11l4 4 9-10"/></svg>
    <div><h4>Professional</h4><p>Inventore veritasis uas<br>vitae dicta sunt</p></div>
  </div>
  <div class="feature" style="left:337px;top:3380px">
    <svg width="32" height="32" viewBox="0 0 24 24" fill="none" stroke="#fff" stroke-width="1.8"><path d="M20 12v8H4V4h11"/><path d="M8 11l4 4 9-10"/></svg>
    <div><h4>Empathetic</h4><p>Inventore veritasis uas<br>vitae dicta sunt</p></div>
  </div>
  <div class="feature" style="left:129px;top:3469px">
    <svg width="32" height="32" viewBox="0 0 24 24" fill="none" stroke="#fff" stroke-width="1.8"><path d="M20 12v8H4V4h11"/><path d="M8 11l4 4 9-10"/></svg>
    <div><h4>Confidential</h4><p>Inventore veritasis uas<br>vitae dicta sunt</p></div>
  </div>
  <div class="feature" style="left:337px;top:3469px">
    <svg width="32" height="32" viewBox="0 0 24 24" fill="none" stroke="#fff" stroke-width="1.8"><path d="M20 12v8H4V4h11"/><path d="M8 11l4 4 9-10"/></svg>
    <div><h4>Expertise</h4><p>Inventore veritasis uas<br>vitae dicta sunt</p></div>
  </div>
  <div class="btn" style="left:129px;top:3563px;width:138px;height:38px">Contact us
    <svg width="16" height="12" viewBox="0 0 16 12" fill="none" stroke="#fff" stroke-width="1.6"><path d="M1 6h13M9 1l5 5-5 5"/></svg>
  </div>
  <svg class="wave" style="top:3672px" height="82" viewBox="0 0 1200 82" preserveAspectRatio="none">
    <path d="M0 64 Q600 -10 1200 64 L1200 82 L0 82Z" fill="#fff"/>
    <path d="M110 40 Q600 -14 1090 40 Q600 6 110 40Z" fill="var(--green)"/>
  </svg>

  <!-- testimonials -->
  <section>
    <p class="eyebrow" style="left:0;width:1200px;text-align:center;top:3786px">Testimonials</p>
    <h2 class="section-title" style="top:3822px;color:var(--navy);font-size:42px">Clients Love Us</h2>
    <div class="quote-box"></div>
    <svg class="abs" style="left:178px;top:3975px" width="150" height="90" viewBox="0 0 150 90"><text x="0" y="150" font-family="Ubuntu,sans-serif" font-size="220" fill="#eef0f3">”</text></svg>
    <p class="abs" style="left:170px;top:3958px;width:860px;text-align:center;font-size:12px;line-height:20px;color:#7b808c">Lorem ipsum dolor sit amet, consectetur adipiscing elit, sed do eiusmod tempor incididunt ut labore et dolore magna aliqua. Ut enim ad minim veniam, quis nostrud exercitation ullamco laboris nisi ut aliquip ex ea commodo consequat. Duis aute irure dolor in reprehenderit inLorem ipsum dolor sit amet, consectetur adipiscing elit, sed do eiusmod tempor incididunt ut labore et dolore Lorem ipsum dolor sit amet, consectetur a dipiscing elit, sed do eiusmod tempor incididunt ut labore et dolore</p>
    <div class="avatar" role="img" aria-label="Client portrait" style="left:428px;top:4086px;width:88px;height:88px"></div>
    <div class="avatar" role="img" aria-label="Client portrait" style="left:684px;top:4086px;width:88px;height:88px;background:linear-gradient(160deg,#c8b8a8,#7a6656)"></div>
    <div class="abs" style="left:536px;top:4062px;width:128px;height:128px;border-radius:50%;border:4px solid var(--green);background:#fff"></div>
    <div class="avatar" role="img" aria-label="Featured client portrait" style="left:545px;top:4071px;width:110px;height:110px;background:linear-gradient(160deg,#dcd6cc,#4b5060)"></div>
    <svg class="abs" style="left:484px;top:4212px" width="28" height="16" viewBox="0 0 28 16" fill="none" stroke="var(--navy)" stroke-width="2"><path d="M27 8H2M8 2L2 8l6 6"/></svg>
    <p class="abs" style="left:500px;top:4208px;width:200px;text-align:center;font-size:17px;color:var(--blue)">Daniel Hartwell</p>
    <svg class="abs" style="left:692px;top:4212px" width="28" height="16" viewBox="0 0 28 16" fill="none" stroke="var(--navy)" stroke-width="2"><path d="M1 8h25M20 2l6 6-6 6"/></svg>
    <svg class="abs" style="left:550px;top:4242px" width="100" height="18" viewBox="0 0 100 18" fill="#f4b625">
      <path id="st" d="M9 1l2.4 5 5.4.7-4 3.8 1 5.4L9 13.3 4.2 15.9l1-5.4-4-3.8 5.4-.7z"/>
      <use href="#st" x="20"/><use href="#st" x="40"/><use href="#st" x="60"/><use href="#st" x="80"/>
    </svg>
  </section>

  <!-- footer -->
  <footer>
    <div class="footer"></div>
    <svg class="wave" style="top:4281px" height="80" viewBox="0 0 1200 80" preserveAspectRatio="none">
      <path d="M0 0 L1200 0 L1200 6 Q600 100 0 6Z" fill="#fff"/>
      <path d="M110 20 Q600 92 1090 20 Q600 74 110 20Z" fill="var(--green)"/>
    </svg>
    <div class="social" style="left:85px;background:#3b5998" aria-label="Social link one"></div>
    <div class="social" style="left:134px;background:#0e76a8" aria-label="Social link two"></div>
    <div class="social" style="left:183px;background:#1da1f2" aria-label="Social link three"></div>
    <div class="social" style="left:232px;background:#e0262e" aria-label="Social link four"></div>
    <div class="abs" style="left:492px;top:4414px;display:flex;align-items:center;gap:12px">
      <span style="width:44px;height:44px;background:var(--white)"></span>
      <span style="font-family:'Ubuntu',sans-serif;font-weight:700;font-size:26px;color:#fff">Corvane Tree Care</span>
    </div>
    <p class="abs" style="left:969px;top:4432px;font-size:14px;font-weight:700;color:#fff">Back to top</p>
    <div class="abs" style="left:1071px;top:4421px;width:42px;height:42px;background:var(--green);display:flex;align-items:center;justify-content:center">
      <svg width="16" height="10" viewBox="0 0 16 10" fill="none" stroke="#fff" stroke-width="2.4"><path d="M2 8l6-6 6 6"/></svg>
    </div>
    <h2 class="abs" style="left:0;top:4563px;width:1200px;text-align:center;font-size:28px;font-weight:500;color:#fff">Get free assessment today</h2>
    <p class="abs" style="left:300px;top:4610px;width:600px;text-align:center;font-size:15px;line-height:25px;color:#fff">Lorem ipsum dolor sit amet, consectetur adipiscing elit, sed do eiusmod tempor incididunt ut labore et dolore magna aliqua.</p>

    <div class="contact-item" style="left:218px">
      <svg width="46" height="46" viewBox="0 0 24 24" fill="none" stroke="var(--green)" stroke-width="1.2"><path d="M22 16.9v3a2 2 0 0 1-2.2 2 19.8 19.8 0 0 1-8.6-3.1 19.5 19.5 0 0 1-6-6A19.8 19.8 0 0 1 2.1 4.2 2 2 0 0 1 4.1 2h3a2 2 0 0 1 2 1.7c.1.9.4 1.8.7 2.7a2 2 0 0 1-.5 2.1L8 9.8a16 16 0 0 0 6 6l1.3-1.3a2 2 0 0 1 2.1-.5c.9.3 1.8.6 2.7.7a2 2 0 0 1 1.7 2z"/></svg>
      <div><small>Make a Call</small><strong>+1-541-555-0192</strong></div>
    </div>
    <div class="abs" style="left:440px;top:4700px;width:1px;height:60px;background:#3a4266"></div>
    <div class="contact-item" style="left:478px">
      <svg width="46" height="46" viewBox="0 0 24 24" fill="none" stroke="var(--green)" stroke-width="1.2"><rect x="2" y="5" width="20" height="15" rx="1"/><path d="M2 6l10 7 10-7M2 20l7-7M22 20l-7-7"/></svg>
      <div><small>Mail Us On</small><strong>hello@corvanetree.com</strong></div>
    </div>
    <div class="abs" style="left:726px;top:4700px;width:1px;height:60px;background:#3a4266"></div>
    <div class="contact-item" style="left:758px">
      <svg width="46" height="46" viewBox="0 0 24 24" fill="none" stroke="var(--green)" stroke-width="1.2"><path d="M12 17s5-5 5-9a5 5 0 0 0-10 0c0 4 5 9 5 9z"/><circle cx="12" cy="8" r="1.8"/><path d="M6 14l-4 8h20l-4-8"/></svg>
      <div><small>Location</small><strong>318 Birchwood Rd</strong></div>
    </div>

    <div class="bottombar">
      <span style="left:83px">Corvane Tree Care</span>
      <span style="left:800px">Privacy Policy</span>
      <span style="left:912px">Terms &amp; Conditions</span>
      <span style="left:1054px">Site Map</span>
    </div>
  </footer>

</div>
</body>
</html>
```